Sterling Oak Renovations, LLC
Long Island Home Remodeling & Design
Professional
Mark Delvecchi
Owner
42 Harlow Avenue
Brentmoor NY 11893
sterlingoakrenovations@mailbox-demo.com
SterlingOakRenovations-demo.com
I would like two business card done. One with a picture for networking events and one w/o for normal use.
I choose two sides only as an option for the photo on the one version. The photo can be on either side, but I would like to see an example of both.
Sterling Oak Renovations, LLC Logo
Mug Shot

```html
<!DOCTYPE html>
<html lang="en">
<head>
<meta charset="utf-8">
<title>Sterling Oak Renovations – Stationery Set</title>
<link href="https://fonts.googleapis.com/css2?family=Open+Sans:wght@400;600;700&display=swap" rel="stylesheet">
<style>
:root{
  --backdrop:#3b3b3d;
  --paper:#ffffff;
  --teal-deep:#1d4a60;
  --teal:#2f7fa3;
  --ink:#4a4f55;
  --rule:#9aa3aa;
  --ghost:#eef1f3;
}
*{box-sizing:border-box;margin:0;padding:0}
html,body{width:1200px;height:410px;overflow:hidden}
body{background:var(--backdrop);font-family:"Open Sans",Arial,sans-serif;color:var(--ink);position:relative}
.piece{position:absolute;background:var(--paper);box-shadow:0 2px 6px rgba(0,0,0,.45);overflow:hidden}

.brand{display:flex;align-items:center;gap:3px;font-weight:700;color:var(--teal);white-space:nowrap;line-height:1}
.brand .mark{width:7px;height:7px;background:var(--teal);flex:none}
.brand.light{color:#fff}
.brand.light .mark{background:#fff}
.tagline{font-size:3px;color:var(--teal);letter-spacing:.2px;white-space:nowrap}
.ghost-name{position:absolute;font-weight:700;color:var(--ghost);line-height:1;text-align:center;width:100%}
.contact{position:absolute;font-size:3px;line-height:1.45;text-align:right;color:var(--ink);white-space:nowrap}

/* envelopes */
.envelope-back{left:34px;top:82px;width:213px;height:103px}
.envelope-back .flap{position:absolute;left:0;top:0;width:100%;height:44px;background:var(--teal-deep)}
.envelope-back .brand{position:absolute;left:50%;top:16px;transform:translateX(-50%);font-size:6px}
.envelope-back .tagline{position:absolute;left:50%;top:28px;transform:translateX(-50%);color:#cfe3ec}
.envelope-front{left:34px;top:233px;width:213px;height:122px}
.envelope-front .brand{position:absolute;left:50%;top:14px;transform:translateX(-50%);font-size:6px}
.envelope-front .tagline{position:absolute;left:50%;top:25px;transform:translateX(-50%)}

/* sheets */
.sheet{top:19px;width:187px;height:365px}
.fax-sheet{left:259px}
.letterhead{left:612px}
.sheet-head{position:absolute;left:0;top:0;width:100%;height:4px;background:var(--teal-deep)}
.sheet .brand{position:absolute;left:8px;top:10px;font-size:5px}
.sheet .tagline{position:absolute;left:8px;top:19px}
.sheet .contact{right:8px;top:9px}
.sheet .ghost-name{top:200px;font-size:40px}
.fax-title{position:absolute;right:12px;top:74px;font-size:9px;font-weight:700;color:var(--ink)}
.fax-table{position:absolute;left:8px;top:88px;width:171px;border-collapse:collapse;font-size:3.5px}
.fax-table td{border:.5px solid var(--rule);height:8px;padding:0 2px}
.fax-table td.label{width:18px;font-weight:600}
.fax-options{position:absolute;left:8px;top:124px;width:171px;display:flex;justify-content:space-between;font-size:3.5px;white-space:nowrap}
.fax-options span::before{content:"";display:inline-block;width:3px;height:3px;border:.5px solid var(--ink);margin-right:2px;vertical-align:middle}

/* business cards */
.card{width:89px;height:54px}
.card-front{left:900px;top:103px}
.card-photo{left:996px;top:103px}
.card-logo{left:900px;top:168px;background:var(--teal-deep)}
.card-plain-back{left:996px;top:168px;background:var(--teal-deep)}
.card .brand{position:absolute;left:5px;top:6px;font-size:4px}
.card .name{position:absolute;left:5px;top:22px;font-size:4px;font-weight:700;color:var(--ink);white-space:nowrap}
.card .role{position:absolute;left:5px;top:27px;font-size:3px}
.card .contact{right:5px;bottom:5px}
.card .portrait{position:absolute;right:5px;top:5px;width:14px;height:18px;background:linear-gradient(#9a8d84,#4b4442)}
.card-logo .brand{left:50%;top:50%;transform:translate(-50%,-50%);font-size:6px}
.card-plain-back .tagline{position:absolute;left:50%;top:50%;transform:translate(-50%,-50%);color:#cfe3ec}

/* large envelope */
.envelope-large{left:886px;top:233px;width:304px;height:151px}
.envelope-large .sheet-head{height:4px}
.envelope-large .brand{position:absolute;left:8px;top:10px;font-size:5px}
.envelope-large .tagline{position:absolute;left:8px;top:19px}
.envelope-large .ghost-name{top:62px;font-size:52px}
</style>
</head>
<body>

<div class="piece envelope-back">
  <div class="flap"></div>
  <div class="brand light"><span class="mark"></span>Sterling Oak Renovations, LLC</div>
  <div class="tagline">Long Island Home Remodeling &amp; Design</div>
</div>

<div class="piece envelope-front">
  <div class="brand"><span class="mark"></span>Sterling Oak Renovations, LLC</div>
  <div class="tagline">Long Island Home Remodeling &amp; Design</div>
</div>

<div class="piece sheet fax-sheet">
  <div class="sheet-head"></div>
  <div class="brand"><span class="mark"></span>Sterling Oak Renovations, LLC</div>
  <div class="tagline">Long Island Home Remodeling &amp; Design</div>
  <div class="contact">42 Harlow Avenue<br>Brentmoor NY 11893<br>Tel 555 010 2740<br>sterlingoakrenovations@mailbox-demo.com<br>SterlingOakRenovations-demo.com</div>
  <div class="fax-title">FAX</div>
  <table class="fax-table">
    <tr><td class="label">To:</td><td></td><td class="label">From:</td><td></td></tr>
    <tr><td class="label">Fax:</td><td></td><td class="label">Pages:</td><td></td></tr>
    <tr><td class="label">Phone:</td><td></td><td class="label">Date:</td><td></td></tr>
    <tr><td class="label">Re:</td><td></td><td class="label">CC:</td><td></td></tr>
  </table>
  <div class="fax-options"><span>Urgent</span><span>For Review</span><span>Please Comment</span><span>Please Reply</span><span>Please Recycle</span></div>
  <div class="ghost-name">SOR</div>
</div>

<div class="piece sheet letterhead">
  <div class="sheet-head"></div>
  <div class="brand"><span class="mark"></span>Sterling Oak Renovations, LLC</div>
  <div class="tagline">Long Island Home Remodeling &amp; Design</div>
  <div class="contact">42 Harlow Avenue<br>Brentmoor NY 11893<br>Tel 555 010 2740<br>sterlingoakrenovations@mailbox-demo.com<br>SterlingOakRenovations-demo.com</div>
  <div class="ghost-name">SOR</div>
</div>

<div class="piece card card-front">
  <div class="brand"><span class="mark"></span>Sterling Oak</div>
  <div class="name">Mark Delvecchi</div>
  <div class="role">Owner</div>
  <div class="contact">42 Harlow Avenue<br>Brentmoor NY 11893<br>SterlingOakRenovations-demo.com</div>
</div>

<div class="piece card card-photo">
  <div class="brand"><span class="mark"></span>Sterling Oak</div>
  <div class="portrait" role="img" aria-label="Portrait photo of Mark Delvecchi"></div>
  <div class="name">Mark Delvecchi</div>
  <div class="role">Owner</div>
  <div class="contact">42 Harlow Avenue<br>Brentmoor NY 11893<br>SterlingOakRenovations-demo.com</div>
</div>

<div class="piece card card-logo">
  <div class="brand light"><span class="mark"></span>Sterling Oak</div>
</div>

<div class="piece card card-plain-back">
  <div class="tagline">Long Island Home Remodeling &amp; Design</div>
</div>

<div class="piece envelope-large">
  <div class="sheet-head"></div>
  <div class="brand"><span class="mark"></span>Sterling Oak Renovations, LLC</div>
  <div class="tagline">Long Island Home Remodeling &amp; Design</div>
  <div class="ghost-name">SOR</div>
</div>

</body>
</html>
```